Dane Morrow films- wedding and event films company website. DESKTOP AND MOBILE

We need a website for a high-end wedding and event film production company. Looking for a very modern and elegant design. my old website is www.danemorrowfilms.example

I like the "white/black/rose gold" color scheme of my logo.

really looking for a sleek modern design the breaths professional and artistic.

Target Market(s)

wedding and event films.

Industry/Entity Type

Film Production

Number of Pages Required

5+ page

Colors

Designer to choose colors to be used in the design.

Requirements
Must have
• website name will be www.danemorrowfilms.example
• tagline is "CINEMATIC STORIES ABOUT YOU"
• sections: HOME, CONTACT, ABOUT, FILMS, BLOG
• You can see my old website at danemorrowfilms.example
• Website about section:
• Dane Morrow Films was Established with the basis of truly cinematic and artistic films in mind. Dane and his team routinely travel the globe documenting weddings and events for high profile clients and discerning couples. Dane was born and raised in Maui Hawaii and has a unique approach to his films that embody the essence of a Hollywood film. Dane has spent the last 10 years traveling the world documenting corporate events and weddings with multiple Award winning production companies. In 2017 Dane decided to establish his own brand “Dane Morrow films” that will take everything he has learned with his past experiences and push it to the next level. Aside from his personal achievements, Dane is extremely passionate about his craft and always looks forward to handcrafting beautiful wedding/event films for his clients. The style of work is non-traditional and the day of filming is extremely unobtrusive (as we are looking for natural-candid/ raw emotions).
• If you are looking for the best price in town, we are probably not the best option, but if you’re looking for the best quality and peace of mind on your wedding day, then you’re in the right place. Dane Morrow Films is a boutique studio that only accepts a limited number of assignments per year. Inquire early to ensure availability.
• LINKS TO VIMEO VIDEOS THAT WILL BE IN THE "FILMS' SECTION.
• BRENT FILM TRAILER - https://clipvault.example/508114362
• BRENT FEATURE FILM - https://clipvault.example/617392048
• JUNE AND ROB'S WEDDING - https://clipvault.example/724958160
• DRONE DEMO REEL - https://clipvault.example/841576203
• WEDDING INDUSTRY EVENT PARTY - https://clipvault.example/962304817/a8d3e7b21c
• images that you can use on site are here: https://brigittolsenimages.proofbox.example/gallery/nora&felix/
• password is: meadow

```html
<!DOCTYPE html>
<html lang="en">
<head>
<meta charset="utf-8">
<title>Dane Morrow films – Cinematic Stories About You</title>
<link href="https://fonts.googleapis.com/css2?family=Poppins:wght@300;400;500;600;700&display=swap" rel="stylesheet">
<style>
:root{
  --rose:#c58a5e;
  --rose-dark:#a86c43;
  --rose-light:#e5b48d;
  --ink:#1d1d1d;
  --text:#555;
  --muted:#777;
  --line:#d9d9d9;
  --white:#fff;
  --black:#000;
}
*{box-sizing:border-box;margin:0;padding:0}
html,body{width:1200px;height:3455px;overflow:hidden;background:var(--white)}
body{font-family:'Poppins',sans-serif;color:var(--ink);position:relative}
a{color:inherit;text-decoration:none}

/* header */
.site-header{position:absolute;top:0;left:0;width:1200px;height:134px;border-bottom:1px solid #eee}
.contact-bar{position:absolute;top:20px;right:100px;display:flex;gap:40px;font-size:14px;color:#333}
.contact-bar span{display:flex;align-items:center;gap:8px}
.brand{position:absolute;left:100px;top:48px;display:flex;align-items:center;gap:12px}
.brand-mark{width:22px;height:22px;background:var(--rose)}
.brand-name{font-size:24px;font-weight:500;letter-spacing:2px;color:#333;text-transform:uppercase}
.main-nav{position:absolute;right:95px;top:86px;display:flex;font-size:14px;color:#222}
.main-nav a{padding:5px 16px 28px}
.main-nav a.active{border-bottom:4px solid var(--rose)}

/* hero */
.hero{position:absolute;top:134px;left:0;width:1200px;height:546px;background:linear-gradient(180deg,#c8c4bd 0%,#8f8b84 40%,#5d5852 75%,#3e3a35 100%)}
.hero-tagline{position:absolute;top:278px;left:0;width:100%;text-align:center;color:var(--white);font-size:29px;font-weight:600;letter-spacing:1px}
.hero-tagline span{display:inline-block;padding:0 6px 10px;border-bottom:1px solid rgba(255,255,255,.7)}
.hero-arrow{position:absolute;top:224px}
.hero-arrow.prev{left:98px}
.hero-arrow.next{right:98px}

/* about card */
.about-card{position:absolute;top:608px;left:99px;width:1002px;height:276px;background:var(--white);box-shadow:0 4px 18px rgba(0,0,0,.18);display:flex}
.about-photo{width:357px;height:100%;background:linear-gradient(135deg,#9a9a9a,#3a3a3a)}
.about-body{padding:40px 40px 0 40px;flex:1}
.section-title{display:flex;align-items:center;gap:14px}
.section-title .mark{width:24px;height:24px;background:var(--rose)}
.section-title h2{font-weight:400;color:#333;white-space:nowrap}
.strip{height:14px;flex:1;background:linear-gradient(90deg,var(--rose-dark),var(--rose-light),var(--rose),var(--rose-light))}
.about-body h2{font-size:30px}
.about-body .strip{margin-right:-51px}
.about-body p{margin-top:16px;font-size:12.6px;line-height:26px;color:var(--text)}

/* testimonial */
.testimonial{position:absolute;top:925px;left:0;width:1200px;text-align:center}
.testimonial blockquote{margin-top:22px;font-size:21px;line-height:28px;color:#333}
.testimonial cite{display:block;margin-top:12px;font-style:normal;font-weight:600;font-size:21px}

/* headings */
.films-heading,.blog-heading{position:absolute;left:104px;width:997px}
.films-heading{top:1090px}
.blog-heading{top:2555px}
.films-heading h2,.blog-heading h2{font-size:30px}

/* films */
.film{position:absolute;left:99px;width:1002px;height:322px;display:flex}
.film.reverse{flex-direction:row-reverse}
.film-media{width:500px;height:100%;position:relative}
.film-media .play{position:absolute;left:50%;top:50%;transform:translate(-50%,-50%)}
.film-info{flex:1;text-align:center;padding:38px 40px 0}
.film-info h3{font-size:27px;font-weight:400;letter-spacing:3px;color:#333}
.film-info h4{margin-top:14px;font-size:16px;font-weight:400;color:#444}
.film-info p{margin-top:12px;font-size:12.6px;line-height:26px;color:var(--text)}
.film-actions{margin-top:18px;display:flex;justify-content:center;gap:12px}
.btn{display:inline-flex;align-items:center;justify-content:center;gap:8px;height:29px;font-size:12.5px}
.btn-download{width:126px;background:var(--rose);color:var(--white)}
.btn-share{width:126px;border:1px solid #555;color:#333;gap:30px}

/* blog */
.blog-list{position:absolute;top:2637px;left:99px;width:1002px;display:flex;justify-content:space-between}
.post{width:311px;text-align:center}
.post-media{height:242px;position:relative}
.post-date{position:absolute;left:18px;top:12px;width:64px;height:88px;background:var(--white);text-align:center;padding-top:6px;line-height:1}
.post-date b{display:block;font-size:30px;font-weight:600}
.post-date span{display:block;font-size:16px;font-weight:600;margin-top:4px}
.post-date small{display:block;font-size:12px;font-weight:600;margin-top:4px}
.post h3{margin-top:26px;font-size:17px;line-height:22px;font-weight:600}
.post p{margin-top:12px;font-size:12.6px;line-height:26px;color:var(--text);padding:0 22px}
.btn-read{margin-top:16px;width:92px;height:32px;background:var(--rose);color:var(--white);font-size:12px}

/* footer */
.site-footer{position:absolute;top:3180px;left:0;width:1200px;height:275px;background:var(--black);color:var(--white);text-align:center}
.footer-brand{margin-top:30px;display:inline-flex;align-items:center;gap:10px;font-size:20px;font-weight:500;letter-spacing:2px;text-transform:uppercase;color:var(--rose)}
.footer-brand i{width:18px;height:18px;background:var(--rose)}
.footer-nav{margin-top:26px;font-size:13px}
.footer-nav a{padding:0 8px}
.social{margin-top:14px;display:flex;justify-content:center;gap:10px}
.social span{width:26px;height:26px;background:#555}
.footer-contact{margin-top:16px;font-size:12px}
.copyright{margin-top:20px;font-size:11px;color:#ccc}
</style>
</head>
<body>

<header class="site-header">
  <div class="contact-bar">
    <span><svg width="16" height="12" viewBox="0 0 16 12"><rect x="0.5" y="0.5" width="15" height="11" fill="none" stroke="#333"/><path d="M1 1l7 6 7-6" fill="none" stroke="#333"/></svg>dane@danemorrowfilms.example</span>
    <span><svg width="14" height="14" viewBox="0 0 14 14"><path d="M3 1l3 3-2 2c1 2 2 3 4 4l2-2 3 3-2 2C5 13 1 9 1 3z" fill="#333"/></svg>808-555-0142</span>
  </div>
  <a class="brand" href="#"><span class="brand-mark"></span><span class="brand-name">Dane Morrow</span></a>
  <nav class="main-nav">
    <a class="active" href="#">Home</a><a href="#">About</a><a href="#">Films</a><a href="#">Blog</a><a href="#">Contact us</a>
  </nav>
</header>

<section class="hero" role="img" aria-label="Bride and groom embracing on a rocky seaside coastline at dusk">
  <svg class="hero-arrow prev" width="16" height="28" viewBox="0 0 16 28"><path d="M14 2L3 14l11 12" fill="none" stroke="#fff" stroke-width="3"/></svg>
  <svg class="hero-arrow next" width="16" height="28" viewBox="0 0 16 28"><path d="M2 2l11 12L2 26" fill="none" stroke="#fff" stroke-width="3"/></svg>
  <h1 class="hero-tagline"><span>CINEMATIC STORIES ABOUT YOU</span></h1>
</section>

<section class="about-card">
  <div class="about-photo" role="img" aria-label="Black and white portrait of the filmmaker"></div>
  <div class="about-body">
    <div class="section-title"><span class="mark"></span><h2>Dane Morrow films</h2><span class="strip"></span></div>
    <p>Dane Morrow Films was Established with the basis of truly cinematic and artistic films in mind. Dane and his team routinely travel the globe documenting weddings and events for high profile clients and discerning couples. Dane was born and raised in Maui Hawaii and has a unique approach to his films that embody the essence of a Hollywood film. Dane has spent the last 10 years traveling the world documenting corporate events and weddings with multiple Award winning production companies.</p>
  </div>
</section>

<section class="testimonial">
  <svg width="28" height="22" viewBox="0 0 28 22"><path d="M0 22V12C0 5 4 1 11 0v4C7 5 6 8 6 11h5v11zM17 22V12c0-7 4-11 11-12v4c-4 1-5 4-5 7h5v11z" fill="#222"/></svg>
  <blockquote>"Dane really is one of the best film makers in Hawaii, great work<br>Dane! We loved the film!"</blockquote>
  <cite>— Mara Quinn</cite>
</section>

<div class="films-heading section-title"><span class="mark"></span><h2>Films</h2><span class="strip"></span></div>

<article class="film" style="top:1177px">
  <div class="film-media" role="img" aria-label="Video still of the bride and groom smiling in a garden" style="background:linear-gradient(135deg,#3c5a34,#7a6a58 55%,#2a2a3a)">
    <svg class="play" width="76" height="76" viewBox="0 0 76 76"><circle cx="38" cy="38" r="35" fill="rgba(0,0,0,.35)" stroke="#fff" stroke-width="4"/><path d="M30 24l22 14-22 14z" fill="#fff"/></svg>
  </div>
  <div class="film-info">
    <h3>B R E N T - FILM TRAILER</h3>
    <h4>Dane Morrow Films</h4>
    <p>Duis aute irure dolor in reprehenderit in voluptate velit esse cillum dolore eu fugiat nulla pariatur. Excepteur sint occaecat cupidatat non proident, sunt in culpa qui officia deserunt mollit anim id est laborum.</p>
    <div class="film-actions">
      <a class="btn btn-download" href="https://clipvault.example/508114362"><svg width="11" height="11" viewBox="0 0 11 11"><path d="M5.5 0v6M2.5 3.5l3 3 3-3M0 10h11" fill="none" stroke="#fff" stroke-width="1.6"/></svg>Download</a>
      <a class="btn btn-share" href="#">Share<svg width="14" height="12" viewBox="0 0 14 12"><path d="M1 6l12-5-3 10-3-4z" fill="none" stroke="#333"/></svg></a>
    </div>
  </div>
</article>

<article class="film reverse" style="top:1518px">
  <div class="film-media" role="img" aria-label="Video still of a bride holding a bouquet by a sunlit window" style="background:linear-gradient(90deg,#6c5a4a,#e9e2d6 45%,#f4efe6 60%,#7a6654)">
    <svg class="play" width="76" height="76" viewBox="0 0 76 76"><circle cx="38" cy="38" r="35" fill="rgba(0,0,0,.35)" stroke="#fff" stroke-width="4"/><path d="M30 24l22 14-22 14z" fill="#fff"/></svg>
  </div>
  <div class="film-info">
    <h3>B R E N T - FEATURE FILM</h3>
    <h4>Dane Morrow Films</h4>
    <p>Duis aute irure dolor in reprehenderit in voluptate velit esse cillum dolore eu fugiat nulla pariatur. Excepteur sint occaecat cupidatat non proident, sunt in culpa qui officia deserunt mollit anim id est laborum.</p>
    <div class="film-actions">
      <a class="btn btn-download" href="https://clipvault.example/617392048"><svg width="11" height="11" viewBox="0 0 11 11"><path d="M5.5 0v6M2.5 3.5l3 3 3-3M0 10h11" fill="none" stroke="#fff" stroke-width="1.6"/></svg>Download</a>
      <a class="btn btn-share" href="#">Share<svg width="14" height="12" viewBox="0 0 14 12"><path d="M1 6l12-5-3 10-3-4z" fill="none" stroke="#333"/></svg></a>
    </div>
  </div>
</article>

<article class="film" style="top:1863px">
  <div class="film-media" role="img" aria-label="Video still of a bride having her makeup done" style="background:linear-gradient(135deg,#4a3526,#a07a5c 50%,#2c2320)">
    <svg class="play" width="76" height="76" viewBox="0 0 76 76"><circle cx="38" cy="38" r="35" fill="rgba(0,0,0,.35)" stroke="#fff" stroke-width="4"/><path d="M30 24l22 14-22 14z" fill="#fff"/></svg>
  </div>
  <div class="film-info">
    <h3>JUNE AND ROB'S WEDDING</h3>
    <h4>Dane Morrow Films</h4>
    <p>Duis aute irure dolor in reprehenderit in voluptate velit esse cillum dolore eu fugiat nulla pariatur. Excepteur sint occaecat cupidatat non proident, sunt in culpa qui officia deserunt mollit anim id est laborum.</p>
    <div class="film-actions">
      <a class="btn btn-download" href="https://clipvault.example/724958160"><svg width="11" height="11" viewBox="0 0 11 11"><path d="M5.5 0v6M2.5 3.5l3 3 3-3M0 10h11" fill="none" stroke="#fff" stroke-width="1.6"/></svg>Download</a>
      <a class="btn btn-share" href="#">Share<svg width="14" height="12" viewBox="0 0 14 12"><path d="M1 6l12-5-3 10-3-4z" fill="none" stroke="#333"/></svg></a>
    </div>
  </div>
</article>

<article class="film reverse" style="top:2206px">
  <div class="film-media" role="img" aria-label="Aerial view of mountain peaks above a forested lake" style="background:linear-gradient(180deg,#6f8fbf 0%,#9fb4cf 30%,#6b5a58 45%,#3f6a3a 65%,#2e5650 100%)">
    <svg class="play" width="76" height="76" viewBox="0 0 76 76"><circle cx="38" cy="38" r="35" fill="rgba(0,0,0,.35)" stroke="#fff" stroke-width="4"/><path d="M30 24l22 14-22 14z" fill="#fff"/></svg>
  </div>
  <div class="film-info">
    <h3>DRONE DEMO REEL</h3>
    <h4>Dane Morrow Films</h4>
    <p>Duis aute irure dolor in reprehenderit in voluptate velit esse cillum dolore eu fugiat nulla pariatur. Excepteur sint occaecat cupidatat non proident, sunt in culpa qui officia deserunt mollit anim id est laborum.</p>
    <div class="film-actions">
      <a class="btn btn-download" href="https://clipvault.example/841576203"><svg width="11" height="11" viewBox="0 0 11 11"><path d="M5.5 0v6M2.5 3.5l3 3 3-3M0 10h11" fill="none" stroke="#fff" stroke-width="1.6"/></svg>Download</a>
      <a class="btn btn-share" href="#">Share<svg width="14" height="12" viewBox="0 0 14 12"><path d="M1 6l12-5-3 10-3-4z" fill="none" stroke="#333"/></svg></a>
    </div>
  </div>
</article>

<div class="blog-heading section-title"><span class="mark"></span><h2>Blog</h2><span class="strip"></span></div>

<section class="blog-list">
  <article class="post">
    <div class="post-media" role="img" aria-label="Bridesmaids posing together in colourful dresses" style="background:linear-gradient(135deg,#8aa08a,#c9b2a2 50%,#b44a4a)">
      <div class="post-date"><b>05</b><span>FEB</span><small>2017</small></div>
    </div>
    <h3>Duis aute irure dolor in reprehenderit in voluptate</h3>
    <p>Duis aute irure dolor in reprehenderit in voluptate velit esse cillum dolore eu fugiat nulla pariatur. Excepteur sint occaecat cupidatat ...</p>
    <a class="btn btn-read" href="#">Read more</a>
  </article>
  <article class="post">
    <div class="post-media" role="img" aria-label="Guests celebrating with drinks by the sea" style="background:linear-gradient(135deg,#a9c3d8,#d7c8b8 50%,#3a4a66)">
      <div class="post-date"><b>05</b><span>FEB</span><small>2017</small></div>
    </div>
    <h3>Duis aute irure dolor in reprehenderit in voluptate</h3>
    <p>Duis aute irure dolor in reprehenderit in voluptate velit esse cillum dolore eu fugiat nulla pariatur. Excepteur sint occaecat cupidatat ...</p>
    <a class="btn btn-read" href="#">Read more</a>
  </article>
  <article class="post">
    <div class="post-media" role="img" aria-label="Coastal village lit up at night" style="background:linear-gradient(180deg,#1c2a44,#26385a 50%,#6a4a2a)">
      <div class="post-date"><b>05</b><span>FEB</span><small>2017</small></div>
    </div>
    <h3>Duis aute irure dolor in reprehenderit in voluptate</h3>
    <p>Duis aute irure dolor in reprehenderit in voluptate velit esse cillum dolore eu fugiat nulla pariatur. Excepteur sint occaecat cupidatat ...</p>
    <a class="btn btn-read" href="#">Read more</a>
  </article>
</section>

<footer class="site-footer">
  <div class="footer-brand"><i></i>Dane Morrow</div>
  <nav class="footer-nav"><a href="#">Home</a>|<a href="#">About</a>|<a href="#">Films</a>|<a href="#">Blog</a>|<a href="#">Contact Us</a></nav>
  <div class="social"><span></span><span></span><span></span><span></span></div>
  <p class="footer-contact">email: dane@danemorrowfilms.example &nbsp;|&nbsp; phone: (808) 555-0142</p>
  <p class="copyright">© 2017 &nbsp;|&nbsp; www.danemorrowfilms.example</p>
</footer>

</body>
</html>
```